VELTRANOVEXA FLOOR CATALOGUE for SPC FLOOR

PROJECT BRIEF – VELTRANOVEXA CATALOG DESIGN
1. Project Overview
Project Title: VELTRANOVEXA Catalog Design
Objective: To create a visually engaging and emotionally connected product catalog that reflects the unique personality The catalog must combine emotional storytelling with practical product presentation.
2. Brand Concept
VELTRANOVEXA is a modern, playful, and colorful brand offering high-quality vinyl flooring. The brand is built 3. Collection Overview
VELTRANOVEXA 5.0
- Hero: Parrot
- Sense: Sight
- Color: Fresh green (#95BF7C)
- Mood: Accessible, youthful, colorful
VELTRANOVEXA 6.0
- Hero: Dolphin
- Sense: Hearing
- Color: Aqua blue (#69B0E6)
- Mood: Calm, precise, fluid
VELTRANOVEXA 7.0
- Hero: Galapagos Tortoise
- Sense: Touch
- Color: Ruby red (#E3344F)
- Mood: Solid, premium, safe
4. Design Objectives
- Integrate hero animals clearly and consistently into each collection section
- Use collection colors as a key visual navigation tool (backgrounds, accents, headers)
- Emphasize the sensory identity of each collection with visual or iconographic references to sight, sound, and touch
- Include room for both emotional storytelling and product specifications
- Communicate the SWAP & JOIN system: all decors available in plank and herringbone formats
5. Visual Style Guidelines
- Typography: Montserrat for headers, Lato for body text
- Layout: modern, clean, consistent grid structure
- Icons: custom-designed line icons for Eye (Sight), Ear (Hearing), Hand (Touch)
- Use illustration or stylized graphic style for animal heroes
- Maintain visual balance between lifestyle/emotion and technical information
6. Deliverables
- Full product catalog layout (A4, print and digital ready)
- Three cover spread layouts (one per collection)
- Icons for sensory experience and product features
- Visual integration of dual format concept (plank + herringbone)
- Consistent styling of all pages, typography, color codes, and image placementsAll details in brief in PDF and some photos like LOGO, already existing materials
Target Market(s)
Europe
Industry/Entity Type
Flooring
Requirements
Must have
- combaine product -SPC Floor with Hero for each collection - animals and with senses - one for each collection.

```html
<!DOCTYPE html>
<html lang="en">
<head>
<meta charset="utf-8">
<title>VELTRANOVEXA 5.0 – Sight</title>
<link rel="stylesheet" href="https://fonts.googleapis.com/css2?family=Montserrat:wght@400;700&family=Lato:ital,wght@0,300;0,700;1,300&display=swap">
<style>
  :root {
    --green-fresh: #95bf7c;
    --green-mid: #6f9a62;
    --green-deep: #1e3530;
    --box-green: rgba(80, 150, 70, 0.78);
    --hero-navy: #0b2236;
    --hero-dark: #03101c;
    --hero-wood: #4a2e1c;
    --hero-red: #c0281c;
    --white: #ffffff;
  }
  * { margin: 0; padding: 0; box-sizing: border-box; }
  html, body { width: 848px; height: 1200px; overflow: hidden; }
  body { font-family: 'Lato', sans-serif; color: var(--white); }

  .cover {
    position: relative;
    width: 848px;
    height: 1200px;
    overflow: hidden;
    background:
      radial-gradient(ellipse 620px 560px at 460px 0px, rgba(149,191,124,0.9), transparent 70%),
      linear-gradient(30deg, var(--green-deep) 0%, #3c5a44 30%, var(--green-mid) 60%, var(--green-fresh) 85%);
  }

  .hero-image { position: absolute; left: 0; top: 0; }

  .collection-title {
    position: absolute;
    top: 84px;
    left: 0;
    width: 848px;
    text-align: center;
    font-family: 'Montserrat', sans-serif;
    font-weight: 700;
    font-size: 38px;
    letter-spacing: 6px;
  }

  .headline {
    position: absolute;
    left: 476px;
    top: 256px;
    font-family: 'Montserrat', sans-serif;
    font-weight: 400;
    font-size: 52px;
    line-height: 62px;
    text-transform: uppercase;
  }

  .justified .line { display: block; text-align: justify; text-align-last: justify; white-space: nowrap; }
  .justified .line.last { text-align-last: left; }

  .story {
    position: absolute;
    left: 478px;
    top: 546px;
    width: 304px;
    font-weight: 300;
    font-style: italic;
    font-size: 20.5px;
    line-height: 27px;
    letter-spacing: 0.6px;
  }

  .sense-box {
    position: absolute;
    left: 417px;
    top: 787px;
    width: 387px;
    height: 74px;
    background: var(--box-green);
    padding: 9px 10px 0 50px;
    font-size: 21.5px;
    line-height: 27px;
    letter-spacing: 0.3px;
    white-space: nowrap;
  }
  .sense-box .sense-icon { position: absolute; left: 20px; top: 18px; }
  .sense-box strong { font-weight: 700; }
  .sense-box em { font-weight: 300; }

  .tagline {
    position: absolute;
    left: 294px;
    top: 936px;
    width: 527px;
    font-weight: 300;
    font-style: italic;
    font-size: 21px;
    line-height: 28px;
    letter-spacing: 1px;
    text-transform: uppercase;
  }
</style>
</head>
<body>
<main class="cover">
  <svg class="hero-image" width="848" height="1200" viewBox="0 0 848 1200" role="img" aria-label="Photograph: scarlet macaw perched on a wooden branch against a dark blue background">
    <defs>
      <linearGradient id="heroTone" x1="0" y1="0" x2="0.6" y2="1">
        <stop offset="0" stop-color="var(--hero-navy)"/>
        <stop offset="0.55" stop-color="var(--hero-dark)"/>
        <stop offset="1" stop-color="var(--hero-wood)"/>
      </linearGradient>
      <radialGradient id="heroWarm" cx="0.2" cy="0.42" r="0.45">
        <stop offset="0" stop-color="var(--hero-red)" stop-opacity="0.75"/>
        <stop offset="1" stop-color="var(--hero-red)" stop-opacity="0"/>
      </radialGradient>
    </defs>
    <circle cx="48" cy="600" r="388" fill="url(#heroTone)"/>
    <circle cx="48" cy="600" r="388" fill="url(#heroWarm)"/>
  </svg>

  <h1 class="collection-title">VELTRANOVEXA 5.0</h1>

  <h2 class="headline">Feel the<br>color.<br>Enjoy<br>the form</h2>

  <p class="story justified">
    <span class="line">Inspired by the vivid world of</span>
    <span class="line">nature, veltranovexa 5.0</span>
    <span class="line">awakens your space with</span>
    <span class="line">energetic and dynamic visuals.</span>
    <span class="line">experience a flooring design</span>
    <span class="line last">that is as expressive as you are.</span>
  </p>

  <div class="sense-box">
    <svg class="sense-icon" width="20" height="14" viewBox="0 0 20 14" aria-hidden="true">
      <path d="M1 7 C4 2 16 2 19 7 C16 12 4 12 1 7 Z" fill="none" stroke="var(--white)" stroke-width="1.8"/>
      <circle cx="10" cy="7" r="2.6" fill="none" stroke="var(--white)" stroke-width="1.8"/>
    </svg>
    <strong>Sense:</strong> <em>sight - visual energy for<br>your space.</em>
  </div>

  <p class="tagline justified">
    <span class="line">Vibrant spaces, bold choices—make your</span>
    <span class="line last">floor a statement</span>
  </p>
</main>
</body>
</html>
```